Company Business Card

I need a Business card designed for my granite company(We install and supply Granite Counter tops). It just needs to have the employee name, title, Store address, email, and phone number. With a nifty logo design and preferably our Maplio map location on the backside. I am not creative so you can go crazy or simple on the logo.
Company Name : The Stone Harbor
Employee Name: Martin Cole
Title: Owner
Address: 4832 Fenwick Oaks Blvd. Dallas, Texas 75391
Email: Martin.Cole@SHBexample.com
Phone: 214-555-0183

```html
<!DOCTYPE html>
<html lang="en">
<head>
<meta charset="utf-8">
<title>The Stone Harbor – Business Card</title>
<link rel="stylesheet" href="https://fonts.googleapis.com/css2?family=Mulish:wght@400;800&display=swap">
<style>
  :root {
    --backdrop: #2b2b2d;
    --card-white: #f6f5f2;
    --ink: #2a2723;
    --ink-soft: #4a4641;
    --brand-rose: #a8706a;
    --brand-light: #f3e6e1;
    --map-base: #ddd6c6;
    --map-light: #e9e4d8;
    --granite-dark: #2a1c1a;
    --granite-mid: #5e3530;
    --granite-red: #8a4a40;
  }
  * { box-sizing: border-box; margin: 0; padding: 0; }
  html, body {
    width: 1200px; height: 1000px; overflow: hidden;
    background: var(--backdrop);
    font-family: "Mulish", Arial, sans-serif;
  }
  .canvas {
    width: 1200px; height: 1000px;
    display: flex; flex-direction: column; align-items: center;
    justify-content: center; gap: 30px;
  }
  .card {
    width: 820px; height: 469px; position: relative;
    border-radius: 6px; overflow: hidden;
  }

  /* Back side */
  .card--back { background: var(--card-white); }
  .map-area {
    position: absolute; left: 20px; top: 20px; width: 540px; height: 270px;
    border-radius: 0 0 28px 0;
    background: linear-gradient(135deg, var(--map-light), var(--map-base));
  }
  .brand-panel {
    position: absolute; left: 600px; top: 80px; width: 190px; height: 175px;
    border-radius: 34px; background: var(--brand-rose);
    display: flex; align-items: center; justify-content: center; text-align: center;
  }
  .brand-panel__name {
    font-weight: 400; font-size: 27px; line-height: 1.15;
    color: var(--brand-light); letter-spacing: 1px; text-transform: uppercase;
  }
  .person {
    position: absolute; right: 30px; top: 272px; text-align: right; color: var(--ink);
    line-height: 1.2;
  }
  .person__name { font-weight: 800; font-size: 28px; letter-spacing: 0.3px; }
  .person__title { font-weight: 400; font-size: 27px; color: var(--ink-soft); }
  .contact {
    position: absolute; color: var(--ink-soft);
    font-size: 24px; font-weight: 400; white-space: nowrap;
  }
  .contact b { font-weight: 800; color: var(--ink); }
  .contact__address { top: 362px; right: 30px; }
  .contact__email { top: 410px; left: 30px; }
  .contact__phone {
    top: 410px; right: 30px; display: flex; align-items: center; gap: 8px;
  }
  .contact__phone svg { width: 22px; height: 22px; }

  /* Front side */
  .card--front { background: var(--granite-dark); }
  .granite-surface {
    position: absolute; inset: 0;
    background: radial-gradient(circle at 45% 45%, var(--granite-red), var(--granite-mid) 55%, var(--granite-dark) 120%);
  }
  .front-panel {
    position: absolute; left: 245px; top: 80px; width: 400px; height: 320px;
    border-radius: 56px; background: var(--brand-rose);
    display: flex; align-items: center; justify-content: center; text-align: center;
  }
  .front-panel__name {
    font-weight: 400; font-size: 50px; line-height: 1.15;
    color: var(--brand-light); letter-spacing: 2px; text-transform: uppercase;
  }
</style>
</head>
<body>
<main class="canvas">
  <section class="card card--back" aria-label="Card back">
    <div class="map-area" role="img" aria-label="Maplio street map showing the store location at 4832 Fenwick Oaks Blvd., Dallas"></div>
    <div class="brand-panel"><p class="brand-panel__name">The<br>Stone<br>Harbor</p></div>
    <div class="person">
      <p class="person__name">Martin Cole</p>
      <p class="person__title">Owner</p>
    </div>
    <p class="contact contact__address">4832 Fenwick Oaks Blvd. Dallas, Texas 75391</p>
    <p class="contact contact__email"><b>e:</b> Martin.Cole@SHBexample.com</p>
    <p class="contact contact__phone">
      <svg viewBox="0 0 24 24" aria-hidden="true">
        <circle cx="12" cy="12" r="11" fill="none" stroke="#2a2723" stroke-width="2"/>
        <path d="M8 6.5c-1 1-1 3 .5 5.5s3.5 4.5 6 5.5c1.5.5 2.5 0 3-1l-2-2-1.5 1c-1.5-.5-3.5-2.5-4-4l1-1.5-2-2.5z" fill="#2a2723"/>
      </svg>
      <span><b>:</b> 214-555-0183</span>
    </p>
  </section>

  <section class="card card--front" aria-label="Card front">
    <div class="granite-surface" role="img" aria-label="Red and black speckled granite texture"></div>
    <div class="front-panel"><p class="front-panel__name">The Stone<br>Harbor</p></div>
  </section>
</main>
</body>
</html>
```